Daily Deals Website Needs a Landing Page (Home Page will act as the landing page)

We need a landing page for a daily deals website that will act as the home page. We have attached the wire frame and logo for reference. Open to creative ideas and suggestions as long as the main elements of the wireframe are incorporated in the design. Need a very simplistic design approach like Vorplex's search page. (www.vorplex.com) . Very clean and distinct CTA's.

Target Market(s)

Customers looking for deals on everyday use items

Font styles to use
Sans Serif

Requirements
Must have
• clean design, lots of white space and strong CTA .
Nice to have
• need a clean design overall. Strong CTA
Should not have
• Cluttered look. Too many colors, keep it simple

```html
<!DOCTYPE html>
<html lang="en">
<head>
<meta charset="utf-8">
<title>Dealvo — Daily Deals</title>
<link href="https://fonts.googleapis.com/css2?family=Arimo:wght@400;700&family=Roboto+Condensed:wght@300;400&family=Montserrat:wght@700&display=swap" rel="stylesheet">
<style>
  :root {
    --navy: #1f3190;
    --green: #5fbf4a;
    --green-tag: #5a9e45;
    --ink: #222222;
    --body: #555555;
    --muted: #9a9a9a;
    --line: #e4e4e4;
    --dark: #111111;
    --footer: #d6d6d7;
    --white: #ffffff;
  }
  * { box-sizing: border-box; margin: 0; padding: 0; }
  html, body { width: 953px; height: 1200px; overflow: hidden; background: var(--white); }
  body { position: relative; font-family: "Arimo", Arial, sans-serif; color: var(--ink); }

  .brand {
    position: absolute; top: 18px; left: 0; width: 953px;
    text-align: center; font-family: "Arimo", Arial, sans-serif;
    font-weight: 700; font-size: 34px; letter-spacing: 1px; color: var(--navy);
  }
  .brand-dot {
    display: inline-block; width: 10px; height: 10px; background: var(--green);
    margin-left: 6px; vertical-align: top; margin-top: 4px;
  }

  .intro {
    position: absolute; top: 102px; left: 88px; width: 777px; height: 85px;
    border: 1px solid var(--line); text-align: center;
  }
  .intro-title { margin-top: 20px; font-size: 20.5px; color: var(--ink); }

  .btn {
    position: absolute; display: flex; align-items: center; justify-content: center;
    background: var(--navy); color: var(--white); border-radius: 22px;
    box-shadow: 0 3px 0 var(--green); font-size: 14px; text-decoration: none;
  }
  .btn-signup { width: 204px; height: 40px; left: 374px; font-size: 14.5px; }
  .btn-signup.top { top: 165px; }
  .btn-signup.bottom { top: 1092px; z-index: 2; }
  .btn-shop { width: 123px; height: 40px; }

  .deal {
    position: absolute; left: 88px; width: 777px; height: 375px;
    background: var(--white); box-shadow: 0 0 4px rgba(0,0,0,0.12);
  }
  .deal-featured { top: 262px; }
  .deal-promoted { top: 665px; }

  .deal-media {
    position: absolute; top: 0; width: 294px; height: 375px;
    background: linear-gradient(155deg, #2a2a2a 0%, #111 45%, #050505 100%);
  }
  .deal-featured .deal-media { left: 0; }
  .deal-promoted .deal-media { right: 0; }
  .product-shape { position: absolute; border-radius: 40px; }
  .deal-featured .product-shape {
    left: 120px; top: 40px; width: 190px; height: 300px;
    background: linear-gradient(160deg, #cfd3d6, #1a8e9e 55%, #0d0d0d);
    opacity: 0.55; border-radius: 60px;
  }
  .deal-promoted .product-shape {
    left: -60px; top: 45px; width: 300px; height: 280px;
    background: linear-gradient(180deg, #6a6a6a, #2b2b2b 60%, #151515);
    opacity: 0.6; border-radius: 140px 140px 40px 40px;
  }

  .tag {
    position: absolute; height: 39px; width: 144px; display: flex; align-items: center;
    justify-content: center; background: var(--green-tag); opacity: 0.95;
    color: var(--white); font-size: 12px; letter-spacing: 0.2px; z-index: 1;
  }
  .deal-featured .tag { left: 0; top: 168px; }
  .deal-promoted .tag { right: 0; top: 168px; }

  .deal-body { position: absolute; top: 0; width: 400px; }
  .deal-featured .deal-body { left: 359px; }
  .deal-promoted .deal-body { left: 35px; }

  .kicker {
    position: absolute; top: 28px; left: 0; padding-left: 5px;
    border-left: 1px solid var(--green); font-size: 11px; line-height: 18px; color: var(--ink);
  }
  .countdown { position: absolute; top: 52px; left: 4px; display: flex; gap: 0; }
  .count { text-align: center; margin-right: 18px; }
  .count-num { display: block; font-size: 15px; color: var(--green); line-height: 18px; }
  .count-label { display: block; font-size: 9.5px; color: var(--body); margin-top: 3px; }

  .offer-line {
    position: absolute; top: 54px; left: 6px; font-family: "Arimo", Arial, sans-serif;
    font-size: 13px; color: var(--ink); letter-spacing: 0.5px;
  }
  .offer-line .pct { color: var(--green); font-size: 24px; margin: 0 3px; }

  .deal-title {
    position: absolute; top: 112px; left: 0; font-size: 20.5px; font-weight: 700;
    color: var(--navy); letter-spacing: 0.3px; white-space: nowrap;
  }
  .deal-text {
    position: absolute; top: 147px; left: 0; width: 380px;
    font-family: "Roboto Condensed", "Arial Narrow", sans-serif; font-weight: 300;
    font-size: 11.4px; line-height: 25px; color: var(--body); text-align: justify;
  }
  .price { position: absolute; top: 263px; left: 4px; font-size: 15.5px; white-space: nowrap; }
  .price-old { color: var(--muted); text-decoration: line-through; margin-left: 10px; font-size: 14.5px; }
  .deal-body .btn-shop { top: 304px; left: -6px; }

  .footer {
    position: absolute; left: 0; top: 1113px; width: 953px; height: 87px; background: var(--footer);
  }
  .copyright {
    position: absolute; top: 56px; width: 100%; text-align: center; font-size: 11px; color: var(--ink);
  }
</style>
</head>
<body>
  <header class="brand">DEALVO<span class="brand-dot"></span></header>

  <section class="intro">
    <h1 class="intro-title" style="font-weight:400">Lorem ipsum dolor sit amet, consectetur adipiscing elit</h1>
  </section>
  <a class="btn btn-signup top" href="#">Daily Emails Singup</a>

  <article class="deal deal-featured">
    <div class="deal-media" role="img" aria-label="Product photo of a smartwatch with a teal and white strap on a dark background">
      <div class="product-shape"></div>
    </div>
    <span class="tag">DEAL OF THE DAY</span>
    <div class="deal-body">
      <p class="kicker">OFFER EXPIRES IN</p>
      <div class="countdown">
        <div class="count"><span class="count-num">000</span><span class="count-label">Days</span></div>
        <div class="count"><span class="count-num">23</span><span class="count-label">Hours</span></div>
        <div class="count"><span class="count-num">15</span><span class="count-label">min</span></div>
        <div class="count"><span class="count-num">55</span><span class="count-label">Sec</span></div>
      </div>
      <h2 class="deal-title">FEATURED DEAL OF THE DAY</h2>
      <p class="deal-text">Lorem ipsum dolor sit amet, consectetur adipiscing elit, sed do eiusmod tempor incididunt ut labore et dolore magna aliqua. Ut enim ad minim veniam, quis nostrud exercitation ullamco laboris nisi ut aliquip ex ea commodo consequat. Duis aute irure dolor in reprehenderit in voluptate velit</p>
      <p class="price">$140.00<span class="price-old">$240.00</span></p>
      <a class="btn btn-shop" href="#">Shop Now</a>
    </div>
  </article>

  <article class="deal deal-promoted">
    <div class="deal-media" role="img" aria-label="Product photo of over-ear headphones on a dark background">
      <div class="product-shape"></div>
    </div>
    <span class="tag">OFFER SALE</span>
    <div class="deal-body">
      <p class="kicker">BUY ONE GET ONE</p>
      <p class="offer-line">EXCLUSIVE <span class="pct">40</span><span style="color:var(--green)">%</span> OFFER</p>
      <h2 class="deal-title">PROMOTED DEAL OF THE DAY</h2>
      <p class="deal-text">Lorem ipsum dolor sit amet, consectetur adipiscing elit, sed do eiusmod tempor incididunt ut labore et dolore magna aliqua. Ut enim ad minim veniam, quis nostrud exercitation ullamco laboris nisi ut aliquip ex ea commodo consequat. Duis aute irure dolor in reprehenderit in voluptate velit</p>
      <p class="price">$140.00<span class="price-old">$240.00</span></p>
      <a class="btn btn-shop" href="#">Shop Now</a>
    </div>
  </article>

  <a class="btn btn-signup bottom" href="#">Daily Emails Singup</a>
  <footer class="footer">
    <p class="copyright">© 2021 All Rights Reserved</p>
  </footer>
</body>
</html>
```